Weightloss company needs Business Card

We want a business card that is clean and professional, yet portrays that we are a friendly, innovative, and versatile program designed to fit the needs of our clients.
I would like there to be 2 sides, one side having an appointment card, and the other side containing the logo and business information. There can be decorations on both sides. The logo is attached.

Target Market(s)

Men and women 40-60

Industry/Entity Type

Business

Contact Information for Business Card

Font styles to use
Sans Serif

Requirements
Must have
• The logo, space for business information
Nice to have
• The colors in the logo
Should not have
• No pictures of people or food

```html
<!DOCTYPE html>
<html lang="en">
<head>
<meta charset="utf-8">
<title>Renewpath Wellness – Business Card</title>
<link rel="stylesheet" href="https://fonts.googleapis.com/css2?family=Open+Sans:wght@400;600;700;800&display=swap">
<style>
  :root{
    --red:#e8203a;
    --blue:#4fc3e8;
    --ink:#111111;
    --paper:#ffffff;
    --backdrop:#e6e6e6;
    --rule:#555555;
  }
  *{box-sizing:border-box;margin:0;padding:0}
  html,body{width:1200px;height:1200px;overflow:hidden}
  body{background:var(--backdrop);font-family:"Open Sans",Arial,sans-serif;color:var(--ink);position:relative}
  .card{position:absolute;width:640px;height:366px;background:var(--paper);overflow:hidden;box-shadow:0 6px 18px rgba(0,0,0,.18)}
  .card svg.rings{position:absolute;left:0;top:0}
  .card--appointment{left:100px;top:150px}
  .card--contact{left:460px;top:660px}

  .appointment{position:absolute;left:64px;top:78px;width:306px}
  .appointment__title{font-weight:700;font-size:19px;line-height:26px;margin:0 0 14px 44px}
  .appointment__row{display:flex;align-items:flex-end;font-size:15px;line-height:20px;margin-bottom:12px}
  .appointment__line{flex:1;border-bottom:1px solid var(--rule);margin:0 4px 4px 4px}
  .appointment__line--blank{border-bottom:0}
  .appointment__line--short{flex:0 0 78px}

  .brand{position:absolute;display:flex;align-items:center;gap:8px;font-weight:800}
  .brand--appointment{right:28px;bottom:96px;font-size:21px;color:var(--ink);line-height:1.05}
  .brand__dot{width:13px;height:13px;border-radius:50%;background:var(--ink);flex:none}

  .person{position:absolute;left:36px;top:44px}
  .person__name{font-weight:800;font-size:27px;color:var(--red);letter-spacing:.5px;line-height:1}
  .person__role{font-size:13px;margin-top:6px}
  .contacts{position:absolute;left:36px;top:136px;list-style:none;font-size:15px}
  .contacts li{display:flex;align-items:center;gap:8px;height:21px}
  .contacts svg{flex:none}
  .address{position:absolute;left:36px;top:246px;font-size:14px;line-height:1.55;text-transform:uppercase}
  .brand--contact{left:395px;top:180px;width:230px;font-size:26px;color:var(--red);line-height:1.05;justify-content:center;text-align:center}
</style>
</head>
<body>

<section class="card card--appointment" aria-label="Appointment side">
  <svg class="rings" width="640" height="366" viewBox="0 0 640 366" aria-hidden="true">
    <circle cx="242" cy="198" r="210" fill="none" stroke="var(--blue)" stroke-width="14"/>
    <circle cx="228" cy="188" r="212" fill="none" stroke="var(--red)" stroke-width="14"/>
  </svg>
  <div class="appointment">
    <h2 class="appointment__title">Next Appointment</h2>
    <div class="appointment__row"><span class="appointment__line appointment__line--blank"></span>Time<span class="appointment__line appointment__line--short"></span></div>
    <div class="appointment__row">Date<span class="appointment__line"></span>Time<span class="appointment__line appointment__line--short"></span></div>
    <div class="appointment__row">Date<span class="appointment__line"></span>Time<span class="appointment__line appointment__line--short"></span></div>
    <div class="appointment__row">Date<span class="appointment__line"></span>Time<span class="appointment__line appointment__line--short"></span></div>
    <div class="appointment__row">Date<span class="appointment__line"></span>Time<span class="appointment__line appointment__line--short"></span></div>
    <div class="appointment__row">Date<span class="appointment__line"></span>Time<span class="appointment__line appointment__line--short"></span></div>
  </div>
  <div class="brand brand--appointment"><span class="brand__dot"></span><span>Renewpath<br>Wellness</span></div>
</section>

<section class="card card--contact" aria-label="Contact side">
  <svg class="rings" width="640" height="366" viewBox="0 0 640 366" aria-hidden="true">
    <circle cx="505" cy="205" r="180" fill="none" stroke="var(--blue)" stroke-width="16"/>
    <circle cx="520" cy="195" r="170" fill="none" stroke="var(--red)" stroke-width="14"/>
    <circle cx="520" cy="195" r="160" fill="var(--ink)"/>
  </svg>
  <div class="person">
    <h1 class="person__name">DANIEL REYES</h1>
    <p class="person__role">CEO</p>
  </div>
  <ul class="contacts">
    <li><svg width="14" height="14" viewBox="0 0 14 14"><circle cx="7" cy="7" r="7" fill="var(--red)"/><path d="M4.5 3.5l1.5 0 .6 2-1 .8a5 5 0 0 0 2.1 2.1l.8-1 2 .6v1.5c-3.5.4-6.4-2.5-6-6z" fill="#fff"/></svg>555-201-4410</li>
    <li><svg width="14" height="14" viewBox="0 0 14 14"><circle cx="7" cy="7" r="7" fill="var(--red)"/><rect x="4.8" y="3" width="4.4" height="8" rx="1" fill="#fff"/></svg>555-388-1926</li>
    <li><svg width="14" height="14" viewBox="0 0 14 14"><circle cx="7" cy="7" r="7" fill="var(--red)"/><rect x="3.5" y="5.5" width="7" height="4" fill="#fff"/><rect x="5" y="3.5" width="4" height="2" fill="#fff"/></svg>555-201-4472</li>
    <li><svg width="14" height="14" viewBox="0 0 14 14"><circle cx="7" cy="7" r="7" fill="var(--red)"/><rect x="3.5" y="4.5" width="7" height="5" fill="#fff"/><path d="M3.5 4.5l3.5 2.8 3.5-2.8" stroke="var(--red)" fill="none" stroke-width=".8"/></svg>daniel.reyes@example.com</li>
  </ul>
  <p class="address">1480 Willow Creek Rd.<br>Suite B. Riverton, TX. 75501</p>
  <div class="brand brand--contact"><span>Renewpath<br>Wellness</span></div>
</section>

</body>
</html>
```